Vista Clinic Needs a Web Design

Designers will use (and improve) our mockups to re-design our mobile-friendly website. We would like to see designs that use the color blue (as our logo in the attached file). The final design should convey convenience and communicate accessible health and wellness.

We need a web design for a company based in Kampala called 'Vista Clinic'.

We help patients to compare health insurance, find a doctor and book an appointment instantly.

Our initial products are Find and Book - a Wordpress database that helps patients to find a doctor and book an appointment instantly; and Insurance - a database that helps patients compare health insurance policies online. We would like to see designs that are mobile-friendly and responsive with awesome user interface and experience.
Updates

Project Deadline Extended Reason: We need web design of 5+ pages. Please see attached files for guidance. Added Wednesday, February 17, 2016

Industry/Entity Type

Health Service

Number of Pages Required

5+ page

Font styles to use
Sans Serif

Colors
33a6d7
85cae6
cee9f5
ecf7fb

Requirements
Must have
• Mobile-friendly and responsive design with awesome UI and UX

```html
<!DOCTYPE html>
<html lang="en">
<head>
<meta charset="utf-8">
<title>Vista Clinic – Find and Book</title>
<link rel="stylesheet" href="https://fonts.googleapis.com/css2?family=Montserrat:wght@300;400;500;600;700&display=swap">
<style>
:root{
  --blue:#33a6d7;
  --blue-soft:#85cae6;
  --blue-pale:#cee9f5;
  --hero-bg:#eef8fb;
  --teal-band:#00afd2;
  --gold-band:#e8b100;
  --tan-band:#cd8d52;
  --ink:#2d2d2d;
  --text:#4a4a4a;
  --muted:#8a8a8a;
  --white:#ffffff;
  --line:#d6d6d6;
}
*{box-sizing:border-box;margin:0;padding:0}
html,body{width:1200px;height:2449px;overflow:hidden}
body{position:relative;font-family:'Montserrat',sans-serif;color:var(--text);background:var(--white)}
.abs{position:absolute}
svg{display:block}

/* header */
.site-header{position:absolute;left:0;top:0;width:1200px;height:66px;background:var(--white)}
.nav-link{position:absolute;top:24px;font-size:11px;color:var(--ink)}
.brand{position:absolute;left:505px;top:17px;display:flex;align-items:center;gap:8px;font-size:17px;font-weight:700;color:var(--ink)}
.brand-dot{width:22px;height:22px;border:2px solid var(--ink);border-radius:50%}
.btn-insurance{position:absolute;left:754px;top:18px;width:80px;height:25px;background:var(--blue);color:var(--white);font-size:11px;font-weight:600;display:flex;align-items:center;justify-content:center}
.auth{position:absolute;left:850px;top:24px;font-size:11px;color:var(--ink)}
.auth span{color:var(--muted);margin:0 6px}

/* hero */
.hero{position:absolute;left:0;top:66px;width:1200px;height:501px;background:var(--hero-bg)}
.hero-title{position:absolute;left:0;width:1200px;top:128px;text-align:center;font-size:23px;font-weight:400;color:var(--blue)}
.search{position:absolute;left:359px;top:176px;width:482px;height:43px;border:2px solid var(--blue);background:var(--white);display:flex}
.search-field{flex:1;display:flex;align-items:center;gap:12px;padding-left:14px;font-size:11px;color:var(--muted)}
.search-btn{width:90px;background:var(--blue);color:var(--white);font-size:11px;font-weight:600;display:flex;align-items:center;justify-content:center}
.mode{position:absolute;top:255px;width:110px;text-align:center;font-size:11px;color:var(--ink)}
.mode-icon{width:56px;height:56px;margin:0 auto 10px;border:1px solid #bfc7ca;border-radius:50%;background:var(--white);display:flex;align-items:center;justify-content:center}
.specialties{position:absolute;left:269px;top:367px;width:660px;height:154px;background:var(--white)}
.specialty{position:absolute;top:22px;width:110px;text-align:center;font-size:11px;color:var(--text)}
.specialty-icon{width:48px;height:48px;margin:0 auto 10px;border:1px solid #dcdcdc;border-radius:50%;display:flex;align-items:center;justify-content:center}
.show-all{position:absolute;left:0;width:660px;top:116px;text-align:center;font-size:9px;font-weight:600;color:var(--muted);letter-spacing:.5px}
.show-all::after{content:"";display:block;width:46px;height:1px;background:var(--line);margin:5px auto 0}

/* apps */
.app-shot{position:absolute;border-radius:18px;background:linear-gradient(180deg,#f5f5f5,#dcdcdc);border:2px solid #cfcfcf}
.app-shot.back{left:379px;top:652px;width:82px;height:226px;background:linear-gradient(180deg,#3a3a3a,#111);border-color:#222}
.app-shot.front{left:430px;top:634px;width:120px;height:256px}
.app-screen{position:absolute;left:8px;top:36px;right:8px;bottom:38px;background:linear-gradient(180deg,#ffffff 0%,#e9f5fb 55%,var(--blue) 80%,#333 100%)}
.app-title{position:absolute;left:598px;top:664px;font-size:22px;font-weight:300;color:var(--ink);line-height:27px}
.app-title b{color:var(--blue);font-weight:600}
.app-note{position:absolute;left:598px;top:769px;font-size:11px;color:var(--muted)}
.store-badge{position:absolute;top:805px;height:33px;background:#111;border-radius:4px}

/* bands */
.band{position:absolute;left:0;width:1200px}
.band-teal{top:936px;height:463px;background:var(--teal-band)}
.band-gold{top:1399px;height:453px;background:var(--gold-band)}
.band-tan{top:1852px;height:503px;background:var(--tan-band)}
.band-title{position:absolute;left:269px;font-size:21px;line-height:26px;color:var(--ink);font-weight:300}
.band-title b{font-weight:600;display:block}
.band-badge{position:absolute;width:50px;height:50px;border:2px solid var(--ink);border-radius:50%;background:var(--white);display:flex;align-items:center;justify-content:center;font-size:20px;font-weight:600;color:var(--ink)}
.strap{position:absolute;left:269px;width:660px;background:var(--ink);color:var(--white);font-size:14px;font-weight:500;text-align:center;display:flex;align-items:center;justify-content:center;line-height:17px}
.feature{position:absolute;display:flex;align-items:flex-start;gap:12px;font-size:11px;line-height:18px;color:var(--ink)}
.feature svg{flex:none}
.offer{position:absolute;left:639px;top:1129px;width:156px;height:156px;border:2px solid var(--white);border-radius:50%;color:var(--white);font-size:12px;font-weight:600;line-height:21px;text-align:center;display:flex;align-items:center;justify-content:center}
.btn-dark{position:absolute;background:var(--ink);font-size:9px;font-weight:600;letter-spacing:.5px;display:flex;align-items:center;justify-content:center}
.panel{position:absolute;border:2px solid var(--ink)}
.panel.light{border-color:var(--white)}
.panel-text{font-size:11px;line-height:16px;color:var(--ink)}
.btn-white{position:absolute;background:var(--white);color:var(--gold-band);font-size:9px;font-weight:600;letter-spacing:.5px;display:flex;align-items:center;justify-content:center}
.phone-profile{position:absolute;left:696px;top:2036px;width:104px;height:214px;border-radius:16px;background:#f4f4f4;border:2px solid #d6d6d6}
.phone-profile .screen{position:absolute;left:6px;top:28px;right:6px;bottom:30px;background:linear-gradient(180deg,#4a8bc4 0%,#e5906a 30%,#ffffff 45%,#ffffff 100%)}

/* footer */
.site-footer{position:absolute;left:0;top:2355px;width:1200px;height:94px;background:var(--white)}
.foot-links{position:absolute;left:269px;top:26px;font-size:9px;color:var(--ink)}
.foot-links span{color:var(--line);margin:0 12px}
.social{position:absolute;right:271px;top:26px;font-size:9px;color:var(--ink);display:flex;gap:12px;align-items:center}
.social i{display:inline-block;width:8px;height:8px;background:var(--ink);margin-right:5px;vertical-align:-1px;font-style:normal}
.copyright{position:absolute;left:269px;top:52px;font-size:7.5px;color:var(--muted)}
</style>
</head>
<body>

<header class="site-header">
  <div class="nav-link" style="left:270px">VC for Doctors</div>
  <div class="nav-link" style="left:390px">Blog</div>
  <div class="brand"><span class="brand-dot"></span>Vista Clinic</div>
  <div class="btn-insurance">Insurance</div>
  <div class="auth">Login<span>|</span>Register</div>
</header>

<section class="hero">
  <h1 class="hero-title" style="top:62px">Find and Book</h1>
  <div class="search" style="top:110px">
    <div class="search-field">
      <svg width="14" height="14" viewBox="0 0 14 14"><circle cx="5.5" cy="5.5" r="4.3" fill="none" stroke="#8a8a8a" stroke-width="1.8"/><line x1="8.6" y1="8.6" x2="13" y2="13" stroke="#8a8a8a" stroke-width="2"/></svg>
      Specialities, Doctors, Clinics, Hospital, Tests etc
    </div>
    <div class="search-btn">Find Doctor</div>
  </div>
  <div class="mode" style="left:453px;top:189px">
    <div class="mode-icon"><svg width="20" height="20" viewBox="0 0 20 20"><rect x="1" y="1" width="18" height="18" fill="none" stroke="#2d2d2d" stroke-width="1.5"/><path d="M10 5v10M5 10h10" stroke="#2d2d2d" stroke-width="1.6"/></svg></div>
    DOCTORS
  </div>
  <div class="mode" style="left:623px;top:189px">
    <div class="mode-icon"><svg width="22" height="24" viewBox="0 0 22 24"><path d="M8 2h6M9 2v7L3 21h16L13 9V2" fill="none" stroke="#2d2d2d" stroke-width="1.5"/><path d="M6 16h10l3 5H3z" fill="#2d2d2d"/></svg></div>
    LAB TESTS
  </div>
  <div class="specialties" style="top:301px">
    <div class="specialty" style="left:17px"><div class="specialty-icon"><svg width="24" height="24" viewBox="0 0 24 24"><circle cx="12" cy="8" r="5" fill="#9a9a9a"/><rect x="4" y="15" width="16" height="7" rx="3" fill="#9a9a9a"/></svg></div>Dentist</div>
    <div class="specialty" style="left:141px"><div class="specialty-icon"><svg width="24" height="24" viewBox="0 0 24 24"><circle cx="12" cy="9" r="6" fill="#9a9a9a"/><rect x="7" y="15" width="9" height="7" fill="#9a9a9a"/></svg></div>Dermetologist</div>
    <div class="specialty" style="left:274px"><div class="specialty-icon"><svg width="26" height="22" viewBox="0 0 26 22"><path d="M13 21S1 13 1 7a6 6 0 0 1 12-1 6 6 0 0 1 12 1c0 6-12 14-12 14z" fill="#9a9a9a"/><path d="M3 10h6l2-4 3 7 2-3h7" fill="none" stroke="#fff" stroke-width="1.5"/></svg></div>Cardiologist</div>
    <div class="specialty" style="left:404px"><div class="specialty-icon"><svg width="24" height="24" viewBox="0 0 24 24"><circle cx="12" cy="10" r="7" fill="#9a9a9a"/><rect x="8" y="16" width="7" height="6" fill="#9a9a9a"/></svg></div>Ear Nose Throat</div>
    <div class="specialty" style="left:525px"><div class="specialty-icon"><svg width="24" height="24" viewBox="0 0 24 24"><circle cx="12" cy="10" r="7" fill="#9a9a9a"/><rect x="9" y="16" width="7" height="6" fill="#9a9a9a"/><circle cx="11" cy="9" r="2.5" fill="#fff"/></svg></div>Psychiatrist</div>
    <div class="show-all">SHOW ALL</div>
  </div>
</section>

<section>
  <div class="app-shot back" role="img" aria-label="Phone showing a list of doctors"></div>
  <div class="app-shot front" role="img" aria-label="Phone showing the Find and Book screen"><div class="app-screen"></div></div>
  <h2 class="app-title">Find a <b>Doctor</b> and <b>Book</b> an<br>appointment in Second!</h2>
  <div class="app-note">Download our Apps.</div>
  <div class="store-badge" style="left:598px;width:104px" role="img" aria-label="App store badge"></div>
  <div class="store-badge" style="left:709px;width:117px" role="img" aria-label="App store badge"></div>
</section>

<section class="band band-teal">
  <h2 class="band-title" style="top:48px"><b>Vista Clinic</b>could save you money</h2>
  <div class="band-badge" style="left:880px;top:53px">$</div>
  <div class="strap" style="top:121px;height:31px">Compare over 8 Health Insurance Providers and get covered today!</div>
  <div class="feature" style="left:405px;top:187px">
    <svg width="28" height="24" viewBox="0 0 28 24"><path d="M1 23V12Q1 3 11 1v4q-5 2-5 7h5v11zM16 23V12q0-9 10-11v4q-5 2-5 7h5v11z" fill="#2d2d2d"/></svg>
    <span>Get a free, no obligation<br>health insurance quote</span>
  </div>
  <div class="feature" style="left:405px;top:252px">
    <svg width="26" height="26" viewBox="0 0 26 26"><circle cx="13" cy="13" r="11.5" fill="none" stroke="#2d2d2d" stroke-width="2"/><circle cx="9" cy="10" r="1.6" fill="#2d2d2d"/><circle cx="17" cy="10" r="1.6" fill="#2d2d2d"/><path d="M7.5 15q5.5 5 11 0" fill="none" stroke="#2d2d2d" stroke-width="2"/></svg>
    <span style="padding-top:4px">Simple and jargon free</span>
  </div>
  <div class="feature" style="left:405px;top:308px">
    <svg width="30" height="26" viewBox="0 0 30 26"><rect x="4" y="1" width="24" height="14" fill="none" stroke="#2d2d2d" stroke-width="2" transform="rotate(-10 16 8)"/><rect x="1" y="9" width="25" height="15" fill="#2d2d2d"/><circle cx="13.5" cy="16.5" r="4" fill="var(--teal-band)"/></svg>
    <span style="padding-top:8px">Low Monthly Payments</span>
  </div>
  <div class="offer" style="top:193px">Take care of your<br>loved ones from<br>UGX 30,000 A<br>Month!</div>
  <div class="btn-dark" style="left:531px;top:383px;width:137px;height:35px;color:var(--teal-band)">COMPARE NOW</div>
</section>

<section class="band band-gold">
  <h2 class="band-title" style="top:48px"><b>Vista Clinic</b>saves you worry</h2>
  <div class="band-badge" style="left:880px;top:52px"><svg width="20" height="20" viewBox="0 0 20 20"><rect x="2" y="4" width="16" height="14" fill="#2d2d2d"/><path d="M6 1v5M14 1v5" stroke="#2d2d2d" stroke-width="2"/><path d="M5 9h10M5 12h10M5 15h10" stroke="#fff" stroke-width="1"/></svg></div>
  <div class="strap" style="top:121px;height:53px">Worry. It never feels good. We'd rather you experience more enjoyable emotions<br>like happiness. Raise funds for your medical cause.</div>
  <div class="panel" style="left:269px;top:219px;width:402px;height:178px">
    <svg class="abs" style="left:38px;top:30px" width="30" height="30" viewBox="0 0 30 30"><path d="M3 8h12M3 8v19h19V15" fill="none" stroke="#2d2d2d" stroke-width="3"/><path d="M11 19l2-6L25 1l4 4-12 12z" fill="#2d2d2d"/></svg>
    <div class="panel-text abs" style="left:80px;top:28px">Create a campaign<br>to raise funds for<br>your medical cause.</div>
    <svg class="abs" style="left:213px;top:34px" width="34" height="24" viewBox="0 0 34 24"><rect x="0" y="0" width="34" height="24" rx="2" fill="#2d2d2d"/><rect x="0" y="6" width="34" height="4" fill="var(--gold-band)"/></svg>
    <div class="panel-text abs" style="left:260px;top:28px">Recive donations to<br>your cause<br>direct to your<br>account</div>
    <div class="btn-dark" style="left:91px;top:115px;width:231px;height:34px;color:var(--gold-band)">START A CAMPAIGN</div>
  </div>
  <div class="panel light" style="left:687px;top:219px;width:242px;height:178px">
    <svg class="abs" style="left:50px;top:30px" width="28" height="28" viewBox="0 0 28 28"><rect x="2" y="9" width="24" height="6" fill="#fff"/><rect x="4" y="15" width="20" height="12" fill="#fff"/><rect x="12" y="9" width="4" height="18" fill="var(--gold-band)"/><path d="M14 9C8 1 3 6 9 9M14 9c6-8 11-3 5 0" fill="none" stroke="#fff" stroke-width="2.2"/></svg>
    <div class="panel-text abs" style="left:101px;top:25px;color:var(--white)">Support any<br>cause or<br>campaign you<br>like</div>
    <div class="btn-white" style="left:51px;top:113px;width:139px;height:36px">DONATE</div>
  </div>
</section>

<section class="band band-tan">
  <h2 class="band-title" style="top:48px"><b>Vista Clinic</b>save your time</h2>
  <div class="band-badge" style="left:880px;top:53px"><svg width="20" height="20" viewBox="0 0 20 20"><rect x="2" y="4" width="16" height="14" fill="none" stroke="#2d2d2d" stroke-width="2"/><path d="M2 8h16" stroke="#2d2d2d" stroke-width="2"/><path d="M6 1v5M14 1v5" stroke="#2d2d2d" stroke-width="2"/></svg></div>
  <div class="strap" style="top:121px;height:31px">We know you don't want to spend all your time waiting in line.</div>
  <div class="feature" style="left:405px;top:202px">
    <svg width="28" height="28" viewBox="0 0 28 28"><rect x="2" y="5" width="24" height="21" fill="none" stroke="#2d2d2d" stroke-width="2.4"/><path d="M2 10h24M8 1v7M20 1v7" stroke="#2d2d2d" stroke-width="2.4"/><path d="M8 17l4 4 8-8" fill="none" stroke="#2d2d2d" stroke-width="2.4"/></svg>
    <span>See Doctor's Shedule</span>
  </div>
  <div class="feature" style="left:405px;top:272px">
    <svg width="26" height="26" viewBox="0 0 26 26"><circle cx="13" cy="13" r="11.5" fill="none" stroke="#2d2d2d" stroke-width="2.2"/><path d="M13 6v7h6" fill="none" stroke="#2d2d2d" stroke-width="2.2"/></svg>
    <span>Choose a time that works<br>for you</span>
  </div>
  <div class="feature" style="left:405px;top:337px">
    <svg width="28" height="24" viewBox="0 0 28 24"><path d="M2 15L16 3l10 6-14 12z" fill="#2d2d2d"/><path d="M2 15v4l10 4 14-12V9" fill="none" stroke="#2d2d2d" stroke-width="2"/></svg>
    <span>Book instantly. No phone calls.<br>No waiting on hold.</span>
  </div>
  <div class="phone-profile" role="img" aria-label="Phone showing a patient health record screen" style="top:184px"><div class="screen"></div></div>
  <div class="btn-dark" style="left:506px;top:427px;width:185px;height:34px;color:var(--gold-band)">BOOK AN APPONTMENT NOW</div>
</section>

<footer class="site-footer">
  <div class="foot-links">About<span>|</span>Contact Us<span>|</span>Privacy Policy</div>
  <div class="social"><span><i></i>Friendspace</span><span style="color:var(--line)">|</span><span><i></i>Chirper</span><span style="color:var(--line)">|</span><span><i></i>Circles+</span></div>
  <div class="copyright">© Copyright 2016 Vista Clinic Limited. All rights reserved.</div>
</footer>

</body>
</html>
```